Artistic Poster for a Short Film

I am the Writer/Director of an upcoming short film called "Driftwater" and I need a 20x30 poster for the project screening. The screening is coming up very soon so apologies for the quick turnaround time. Here is a short synopsis:

"Walter is a mysterious man who is lost and disoriented. With the help of Marisol, he searches for items out of an old diary written long ago by a woman named Gloria, despite not understanding exactly why he does so. Marisol helps, but when they are unsuccessful she confronts Walter: Does he know why he restlessly searches for these items? The truth is shocking, and reveals Walter's connections to Marisol, Gloria, and the strange old diary.

The truth is that Walter is actually an old man, and Marisol is his caretaker and granddaughter. His memories, including those of Gloria, his deceased wife, have been destroyed by Dementia. He often wakes believing himself to be at an earlier stage of his life, and therefore meets many of the challenges of life with anger and confusion."

Here is the film's website: http://www.driftwater-film.example
Here is our successful Fundbarrow: http://www.fundbarrow.example/projects/502847719/driftwater-a-short-film

The design should be dark and simple. I'm a fan of the art-prints that this short film used (scroll down to see): http://www.fundbarrow.example/projects/ruthvanderlo/kettle-a-short-film-based-on-the-story-by-omar-quill but I'm also open to other ideas. If you google "alternative movie posters" you'll see what I mean. The poster should be simple, easy to read, and hint at the themes of the film without giving the twist away.

Here is a link to the Fine Cut of the film: https://clipvault.example/48210576 The password is: lanterns72
It is not a completed version but will give you an idea of what the film will look like.

Target Market(s)

The intended audience is an art-film crowd of moviegoers.

Industry/Entity Type

Movie

Requirements
Must have
• The poster must have the typical movie poster text at the bottom. The information that should be included is: First line: COPPER LANTERN STUDIOS presents a film by DANIEL OSTROM "DRIFTWATER" MARCEL BRUNAUD TERRA WOLCOTT
Second line: music by OWEN PRATT director of photography VICTOR L. MORALES edited by SIMON ORR costume designer ROBERTA CLINE
Third line: produced by GAIL TORVALD DANIEL OSTROM written and directed by DANIEL OSTROM

It should have the title of the film "Driftwater" and "A film by Daniel Ostrom" on the poster (in addition to the text at the bottom.

It must be high-quality and printable to a size of 20x30. Ideal resolution is 6060x9090. I only need the high quality printable file, I will do the printing myself.
Should not have
• Bright colors.

```html
<!DOCTYPE html>
<html lang="en">
<head>
<meta charset="utf-8">
<title>Driftwater — a film by Daniel Ostrom</title>
<link rel="stylesheet" href="https://fonts.googleapis.com/css2?family=Cinzel:wght@500;600&family=Didact+Gothic&family=Josefin+Sans:wght@400;600;700&display=swap">
<style>
  :root {
    --sky-deep: #16242e;
    --sky-mid: #3d5866;
    --cloud-light: #a9bfc4;
    --cloud-soft: #7d97a0;
    --moon-core: #f3f8e8;
    --moon-halo: #cfe2d4;
    --mist: #6c8794;
    --ground-mist: #34495a;
    --ground-dark: #0c1418;
    --title-ink: #241d1b;
    --credit-ink: #f4f4f0;
  }
  * { margin: 0; padding: 0; box-sizing: border-box; }
  html, body {
    width: 1200px;
    height: 900px;
    overflow: hidden;
    background: var(--ground-dark);
  }
  .poster {
    position: relative;
    width: 1200px;
    height: 900px;
    overflow: hidden;
  }
  .poster-scene {
    position: absolute;
    inset: 0;
    background:
      radial-gradient(circle 105px at 645px 340px, var(--moon-core) 0%, var(--moon-core) 55%, rgba(207,226,212,0.85) 80%, rgba(207,226,212,0) 100%),
      radial-gradient(ellipse 300px 230px at 645px 340px, rgba(207,226,212,0.7) 0%, rgba(160,190,192,0.25) 60%, rgba(160,190,192,0) 100%),
      radial-gradient(ellipse 260px 120px at 300px 300px, rgba(169,191,196,0.55) 0%, rgba(169,191,196,0) 100%),
      radial-gradient(ellipse 280px 140px at 1000px 230px, rgba(169,191,196,0.5) 0%, rgba(169,191,196,0) 100%),
      radial-gradient(ellipse 320px 110px at 640px 80px, rgba(125,151,160,0.55) 0%, rgba(125,151,160,0) 100%),
      radial-gradient(ellipse 260px 100px at 180px 130px, rgba(125,151,160,0.35) 0%, rgba(125,151,160,0) 100%),
      radial-gradient(ellipse 700px 90px at 600px 600px, rgba(108,135,148,0.85) 0%, rgba(108,135,148,0) 100%),
      radial-gradient(ellipse 320px 500px at 0px 450px, rgba(22,36,46,0.8) 0%, rgba(22,36,46,0) 100%),
      radial-gradient(ellipse 320px 500px at 1200px 450px, rgba(22,36,46,0.7) 0%, rgba(22,36,46,0) 100%),
      linear-gradient(180deg, var(--sky-deep) 0%, var(--sky-mid) 22%, var(--cloud-soft) 42%, var(--sky-mid) 55%, var(--mist) 66%, var(--ground-mist) 76%, #1b2831 86%, var(--ground-dark) 100%);
  }
  .film-title {
    position: absolute;
    top: 150px;
    left: 0;
    width: 1200px;
    padding-left: 60px;
    text-align: center;
    font-family: "Cinzel", serif;
    font-weight: 600;
    font-size: 86px;
    line-height: 1.2;
    letter-spacing: 1px;
    color: var(--title-ink);
    text-shadow: 2px 3px 4px rgba(0,0,0,0.35);
  }
  .film-byline {
    position: absolute;
    top: 292px;
    right: 140px;
    display: flex;
    align-items: baseline;
    gap: 22px;
    font-family: "Josefin Sans", sans-serif;
    color: var(--title-ink);
  }
  .film-byline__lead {
    font-size: 20px;
    font-weight: 600;
    letter-spacing: 4px;
  }
  .film-byline__name {
    font-size: 38px;
    font-weight: 700;
    letter-spacing: 5px;
  }
  .billing-block {
    position: absolute;
    left: 0;
    top: 712px;
    width: 1200px;
    text-align: center;
    font-family: "Didact Gothic", sans-serif;
    color: var(--credit-ink);
  }
  .billing-line {
    font-size: 19px;
    line-height: 1;
    white-space: nowrap;
    margin-bottom: 34px;
  }
  .billing-line strong {
    font-family: "Josefin Sans", sans-serif;
    font-weight: 600;
    font-size: 20px;
  }
</style>
</head>
<body>
  <main class="poster">
    <div class="poster-scene" role="img" aria-label="Misty moonlit field at night under heavy clouds: a lone figure stands between rows of pale power poles and sagging wires, an open umbrella lies tipped in the grass at right"></div>

    <h1 class="film-title">DRIFTWATER</h1>

    <p class="film-byline">
      <span class="film-byline__lead">A FILM BY</span>
      <span class="film-byline__name">DANIEL OSTROM</span>
    </p>

    <footer class="billing-block">
      <p class="billing-line"><strong>COPPER LANTERN STUDIOS</strong> presents a film by <strong>DANIEL OSTROM</strong> <strong>"DRIFTWATER"</strong> <strong>MARCEL BRUNAUD</strong> <strong>TERRA WOLCOTT</strong></p>
      <p class="billing-line">Music by <strong>OWEN PRATT</strong> director of photography <strong>VICTOR L. MORALES</strong> edited by <strong>SIMON ORR</strong> costume designer <strong>ROBERTA CLINE</strong></p>
      <p class="billing-line">Produced by <strong>GAIL TORVALD</strong> <strong>DANIEL OSTROM</strong> written and directed by <strong>DANIEL OSTROM</strong></p>
    </footer>
  </main>
</body>
</html>
```